Fundraiser Flyer and Email Template

We are looking for a flexible coordinated flyer and email template. The feel of both should be more formal or professional. We are not looking for an overly "political" design that features American flags or other "political" symbols.

We are a political fundraising firm that works with elected officials to set up fundraisers for their campaigns. We send the invites to these events via US Mail and email, so we are looking for a standardized template that will work as both an 8.5 x 11 inch printed flyer, as well as an email template.

The information in the email will be text, but images can be used for formatting.

Some clients have a campaign logo, others do not. The format should be flexible enough to either include the logo, or leave it out. Size also varies.

Any colors in the template should be editable so we can match logos as we get them.

We're open to any format that allows us to edit the format as needed. This would include Photoshop, Microsoft Word, etc.

The text of the invite should include space for:

---------------------------------------
NAME
DISTRICT NUMBER AND OFFICE

DATE OF EVENT
TIME OF EVENT

LOCATION
LOCATION ADDRESS
LOCATION CITY, STATE, ZIP

SUGGESTED CONTRIBUTION LEVELS (Typically 3 levels are provided such as Gold: $1,000, Silver: $500, Bronze: $250)

ADDRESS TO SEND CHECKS TO

RSVP CONTACT INFORMATION

The invite will also need fine-print at the bottom that reads:
"Pennsylvania law allows personal, partnership, and PAC contributions. By law we cannot accept corporate contributions
Paid for by [NAME]"

It Professional

Serif
Sans Serif

• Must have spaces for:
• NAME
• DISTRICT NUMBER AND OFFICE
• DATE OF EVENT
• TIME OF EVENT
• LOCATION
• LOCATION ADDRESS
• LOCATION CITY, STATE, ZIP
• SUGGESTED CONTRIBUTION LEVELS (Typically 3 levels are provided such as Gold: $1,000, Silver: $500, Bronze: $250)
• ADDRESS TO SEND CHECKS TO
• RSVP CONTACT INFORMATION
• The invite will also need fine-print at the bottom that reads:
• "Pennsylvania law allows personal, partnership, and PAC contributions. By law we cannot accept corporate contributions
• Paid for by [NAME]"
• It should not be overly "political".

```html
<!DOCTYPE html>
<html lang="en">
<head>
<meta charset="utf-8">
<title>Fundraiser Invitation</title>
<link rel="stylesheet" href="https://fonts.googleapis.com/css2?family=Bebas+Neue&family=Roboto+Condensed:wght@400&display=swap">
<style>
  :root {
    --paper-light: #f1f1f2;
    --paper-mid: #d2d2d4;
    --ink-black: #1c1c1e;
    --ink-dark: #232325;
    --accent-blue: #0aa6e6;
    --band-blue: #00a2e4;
    --periwinkle: #6f7cf5;
    --lavender: #aab0ea;
    --lavender-pale: #d9dcfb;
    --stripe-grey: #bdbdc0;
    --text-white: #ffffff;
    --gold: #e4b93a;
    --silver: #c9c9cc;
    --bronze: #b98a55;
  }
  * { margin: 0; padding: 0; box-sizing: border-box; }
  html, body { width: 950px; height: 1200px; overflow: hidden; background: #ffffff; }
  .flyer {
    position: relative;
    width: 950px;
    height: 1200px;
    overflow: hidden;
    background: radial-gradient(ellipse at 50% 40%, var(--paper-light) 0%, var(--paper-mid) 100%);
    font-family: "Bebas Neue", "Arial Narrow", sans-serif;
  }
  .layout-art { position: absolute; inset: 0; width: 950px; height: 1200px; }
  .event-title {
    position: absolute; left: 118px; top: 146px;
    font-size: 140px; line-height: 1; color: var(--accent-blue); font-weight: 400;
    white-space: nowrap;
  }
  .event-title .word-the { letter-spacing: 3px; margin-right: 36px; }
  .event-title .word-event { letter-spacing: 56px; }
  .district {
    position: absolute; left: 196px; top: 292px;
    font-size: 48px; line-height: 1; color: var(--ink-black); letter-spacing: 5px;
    white-space: nowrap;
  }
  .tag {
    position: absolute; color: var(--text-white); font-size: 66px; line-height: 1;
    letter-spacing: 4px; transform: rotate(-5deg); transform-origin: left center;
    white-space: nowrap;
  }
  .tag-date { left: 60px; top: 428px; }
  .tag-time { left: 538px; top: 382px; }
  .venue { position: absolute; left: 0; width: 950px; top: 540px; text-align: center; }
  .venue-line { font-size: 40px; line-height: 50px; color: var(--ink-black); letter-spacing: 0.5px; }
  .contribution { position: absolute; left: 0; width: 950px; top: 706px; text-align: center; }
  .contribution-title { font-size: 62px; line-height: 62px; color: var(--accent-blue); letter-spacing: 0.5px; font-weight: 400; }
  .contribution-note { font-size: 31px; line-height: 34px; color: var(--text-white); }
  .contribution-levels { font-size: 38px; line-height: 42px; color: var(--text-white); }
  .level-gold { color: var(--gold); }
  .level-silver { color: var(--silver); }
  .level-bronze { color: var(--bronze); }
  .sep { color: var(--text-white); margin: 0 8px; }
  .sep-bronze { color: var(--bronze); margin: 0 8px; }
  .response { position: absolute; left: 0; width: 950px; top: 888px; text-align: center; }
  .response-line { font-size: 50px; line-height: 56px; color: var(--text-white); letter-spacing: 0.5px; }
  .fine-print {
    position: absolute; left: 32px; top: 1069px; width: 878px; height: 110px;
    border: 1.5px dashed var(--accent-blue); border-radius: 20px;
    display: flex; align-items: center; justify-content: center; text-align: center;
    padding: 0 22px;
    font-family: "Roboto Condensed", "Arial Narrow", sans-serif;
    font-size: 25px; line-height: 32px; color: var(--text-white);
  }
</style>
</head>
<body>
<main class="flyer">
  <svg class="layout-art" viewBox="0 0 950 1200" aria-hidden="true">
    <defs>
      <linearGradient id="headerTone" x1="0" y1="0" x2="1" y2="0">
        <stop offset="0" stop-color="var(--periwinkle)"/>
        <stop offset="1" stop-color="var(--lavender-pale)"/>
      </linearGradient>
    </defs>

    <!-- header art area -->
    <g role="img" aria-label="Header frame artwork in periwinkle and lavender tones">
      <polygon points="0,0 950,0 950,100 0,132" fill="url(#headerTone)" opacity="0.75"/>
    </g>

    <!-- soft accent strips -->
    <g role="img" aria-label="Directional stripe artwork in soft grey">
      <polygon points="0,380 460,350 460,362 0,392" fill="var(--stripe-grey)" opacity="0.8"/>
      <polygon points="430,496 950,448 950,460 430,508" fill="var(--stripe-grey)" opacity="0.8"/>
    </g>

    <!-- date and time bars -->
    <polygon points="0,420 465,392 472,472 0,514" fill="var(--ink-dark)"/>
    <polygon points="490,387 943,345 950,420 498,462" fill="var(--ink-dark)"/>

    <!-- venue dividers -->
    <line x1="267" y1="584" x2="679" y2="584" stroke="var(--periwinkle)" stroke-width="1"/>
    <line x1="267" y1="634" x2="679" y2="634" stroke="var(--periwinkle)" stroke-width="1"/>

    <!-- dark lower field -->
    <polygon points="0,676 472,700 950,676 950,1200 0,1200" fill="var(--ink-dark)"/>
    <polyline points="0,676 472,700 950,676" fill="none" stroke="var(--lavender)" stroke-width="3"/>

    <!-- blue response band -->
    <polygon points="0,834 472,860 950,834 950,842 472,868 0,842" fill="var(--paper-mid)"/>
    <polygon points="0,842 472,868 950,842 950,1003 472,1036 0,1003" fill="var(--band-blue)"/>
    <polygon points="0,1003 472,1036 950,1003 950,1011 472,1044 0,1011" fill="#e6e6e8"/>
  </svg>

  <h1 class="event-title"><span class="word-the">THE</span><span class="word-event">EVENT</span></h1>
  <p class="district">DISTRICT NUMBER AND OFFICE</p>

  <p class="tag tag-date">DATE OF EVENT</p>
  <p class="tag tag-time">TIME OF EVENT</p>

  <section class="venue">
    <p class="venue-line">LOCATION GOES HERE</p>
    <p class="venue-line">LOCATION ADDRESS GOES HERE</p>
    <p class="venue-line">LOCATION CITY, STATE, ZIP</p>
  </section>

  <section class="contribution">
    <h2 class="contribution-title">SUGGESTED CONTRIBUTION LEVELS</h2>
    <p class="contribution-note">(TYPICALLY 3 LEVELS ARE PROVIDED SUCH AS</p>
    <p class="contribution-levels"><span class="level-gold">GOLD: $1,000</span><span class="sep">|</span><span class="level-silver">SILVER: $500</span><span class="sep-bronze">|</span><span class="level-bronze">BRONZE: $250)</span></p>
  </section>

  <section class="response">
    <p class="response-line">ADDRESS TO SEND CHECKS TO_GOES HERE</p>
    <p class="response-line">RSVP CONTACT INFORMATION_GOES HERE</p>
  </section>

  <p class="fine-print">"Pennsylvania law allows personal, partnership, and PAC contributions. By law we cannot accept corporate contributions Paid for by [NAME]</p>
</main>
</body>
</html>
```